School website design - Technology and the arts

We will need a new or updated design that incorporates the following features:
-Reactive design that changes with the needs of the device.
-Static Background - only content scrolls
-Static Menu - similar to the Pressly Harbor Lantern theme
-Alert box for important notices (closings/emergency use only) that doesn’t display unless active
-Margins must be wider than “standard pressly theme” (fits the entire display at any resolution, doesn’t just center a columned design)
-Features an image scroll on the front page to show our current works/progress. (only if the screen is big enough). Should have swipe capability
-We must have a place on the front page to display the current school news as well as a location to display current events with a poster (see current webdesign for example)
-Uses the school colors (green and gold/yellow) in a way that is pleasing to the eye.
-Unique design to our school that is very clean and modern.
-Events need to be able to pop-out when you mouseover in a desktop environment. Example: http://skinvault.example/category/pressly/creative (mouse over a theme and it shows additional information about it without a refresh)
-Custom Admin panel to easily updated the news and events section.
-Notes: We are currently using some free icons that we found to make the current site look not so boring since we do not have a lot of content on each page. We would like to step away from that and are open to suggestions. Possibly something like http://vormlab.example/demo/?theme=arch under the services section but smaller.
-Notes 2: We have plenty of pictures of our building and activities that can be used as a background, etc.
-We are open to new ideas and suggestions.

Our current website is https://www.kelmont-academy.example to get an idea on how we manage our current site.

```html
<!DOCTYPE html>
<html lang="en">
<head>
<meta charset="utf-8">
<title>Kelmont Regional Academy</title>
<link href="https://fonts.googleapis.com/css2?family=UnifrakturMaguntia&family=Open+Sans:wght@300;400;600;700&family=Arimo:wght@400;700&family=Oswald:wght@300;400&display=swap" rel="stylesheet">
<style>
:root{
  --green:#1f5a1f;
  --green-dark:#1a4f1a;
  --gold:#f9bf00;
  --gold-card:#fdd036;
  --gold-text:#f5c400;
  --red:#a8123a;
  --grey:#666;
  --white:#fff;
}
*{margin:0;padding:0;box-sizing:border-box}
html,body{width:680px;height:1200px;overflow:hidden;background:var(--white)}
body{position:relative;font-family:"Arimo",Arial,sans-serif;color:var(--grey)}
.abs{position:absolute}
.blackletter{font-family:"UnifrakturMaguntia",serif;color:var(--green);font-weight:400}

.crest{left:76px;top:14px;width:66px;height:66px;border-radius:50%;background:var(--green)}
.site-title{left:165px;top:18px;font-size:26px;line-height:26px}
.tagline{left:167px;top:74px;font-family:"Open Sans",sans-serif;font-size:6.5px;color:#555}
.toplinks{left:510px;top:47px;font-size:6px;color:var(--green);display:flex;gap:6px;white-space:nowrap}
.search{left:467px;top:61px;width:124px;height:18px;background:var(--gold);font-size:6.5px;color:#333;padding:5px 5px}
.search-btn{left:591px;top:61px;width:21px;height:18px;background:var(--green)}

.band{left:0;top:96px;width:680px;height:221px;background:var(--green)}
.nav{left:67px;top:96px;height:23px;display:flex;font-size:8px;color:var(--gold-text)}
.nav span{padding:7px 13px}
.nav .active{background:var(--gold);color:var(--green);padding:7px 14px}
.hero-frame{left:65px;top:125px;width:550px;height:233px;background:var(--white)}
.hero{left:68px;top:129px;width:544px;height:226px;background:linear-gradient(120deg,#2a2c2a,#8a8c88 50%,#d9d6cc)}

.welcome{left:70px;top:374px;font-size:26px}

.mission{left:70px;top:423px;width:263px;height:250px;background:var(--green)}
.mission-photo{left:77px;top:430px;width:246px;height:137px;border:3px solid var(--gold);background:linear-gradient(135deg,#3a2a1e,#a27a5e 55%,#4c3526)}
.mission h2{position:absolute;left:8px;top:155px;font-family:"Open Sans",sans-serif;font-weight:300;font-size:17px;color:var(--white)}
.mission p{position:absolute;left:9px;top:182px;width:246px;font-family:"Open Sans",sans-serif;font-size:6.6px;line-height:8.7px;color:var(--white)}
.mission .more{top:232px;font-weight:700;font-size:7px}

.news{left:350px;width:262px;height:60px}
.date{position:absolute;left:0;top:0;width:42px;height:50px;text-align:center;font-family:"Oswald",sans-serif}
.date b{display:block;font-weight:400;font-size:21px;line-height:21px;padding-top:7px}
.date i{display:block;font-style:normal;font-size:7.5px;line-height:10px;margin-top:4px}
.date.green{background:var(--green);color:var(--gold-text)}
.date.gold{background:var(--gold);color:var(--green)}
.date::after{content:"";position:absolute;right:-7px;top:8px;border:5px solid transparent;border-left:7px solid;border-right:0}
.date.green::after{border-left-color:var(--green)}
.date.gold::after{border-left-color:var(--gold)}
.news h3{position:absolute;left:60px;top:0;width:200px;font-family:"Open Sans",sans-serif;font-weight:700;font-size:10.5px;line-height:12px;color:var(--green)}
.news p{position:absolute;left:61px;width:200px;font-size:7px;line-height:8.7px;color:#666}
.news a{position:absolute;left:61px;font-size:7px;color:var(--red);text-decoration:none}

.events{left:0;top:718px;width:680px;height:304px;background:var(--gold)}
.notch{left:332px;top:718px;width:0;height:0;border:8px solid transparent;border-top:8px solid var(--white)}
.events-title{left:0;top:752px;width:680px;text-align:center;font-size:26px}
.card{width:263px;height:83px;background:var(--gold-card)}
.thumb{position:absolute;left:10px;top:10px;width:60px;height:46px}
.card h3{position:absolute;left:75px;top:8px;width:180px;font-family:"Open Sans",sans-serif;font-weight:700;font-size:10.5px;line-height:11px;color:var(--green)}
.card .when{position:absolute;left:75px;top:32px;font-size:7px;font-weight:700;color:var(--red)}
.card p{position:absolute;left:75px;top:50px;width:180px;font-size:7px;line-height:8.7px;color:#555}

.footer{left:0;top:1022px;width:680px;height:150px;background:var(--green)}
.fcol{top:1053px;color:#cfd9cf;font-family:"Open Sans",sans-serif}
.fcol h4{font-weight:600;font-size:13.5px;color:var(--white);margin-bottom:6px;letter-spacing:.2px}
.fcol ul{list-style:none;font-size:7.6px;line-height:10.3px}
.fcol .addr{font-size:6.6px;line-height:10px}
.phone{font-family:"Oswald",sans-serif;font-weight:300;font-size:15px;color:#cfd9cf;margin-top:4px;display:flex;align-items:center;gap:5px}

.copyright{left:73px;top:1183px;font-size:6.5px;color:var(--green)}
.social{left:533px;top:1180px;display:flex;gap:4px}
.social span{width:13px;height:13px;border-radius:50%;background:var(--green)}
</style>
</head>
<body>

<header>
  <div class="abs crest"></div>
  <div class="abs site-title blackletter">Kelmont Regional<br>Academy</div>
  <div class="abs tagline">for the arts &amp; technology | 48 Linden Row, 40217 555.018.4420</div>
  <div class="abs toplinks"><span>KRA Email</span><span>Calendars</span><span>Contact Us</span></div>
  <div class="abs search">search site ...</div>
  <div class="abs search-btn">
    <svg width="21" height="18" viewBox="0 0 21 18"><circle cx="11.5" cy="7.5" r="3" fill="none" stroke="#fff" stroke-width="1.5"/><line x1="9.3" y1="9.7" x2="6.5" y2="12.5" stroke="#fff" stroke-width="2"/></svg>
  </div>
</header>

<div class="abs band"></div>
<nav class="abs nav">
  <span class="active">Home</span><span>ABOUT KRA</span><span>Students/Parents</span><span>Faculty/Staff</span><span>Documents/Forms</span><span>Programs of Study</span><span>Services</span>
</nav>
<div class="abs hero-frame"></div>
<div class="abs hero" role="img" aria-label="Photo of a student drawing at a drafting table"></div>

<h1 class="abs welcome blackletter">Welcome to Our School</h1>

<section class="abs mission">
  <h2>Our Mission</h2>
  <p>Kelmont Regional Academy for the Arts and Technology provides gifted and talented students a differentiated and rigorous education, cultivates a supportive environment that inspires unique artistic and technological visions, promotes cultural tolerance, nurtures community partnerships, and produces active, engaged citizens.</p>
  <p class="more">Learn More</p>
</section>
<div class="abs mission-photo" role="img" aria-label="Photo of cheering students at a school rally"></div>

<article class="abs news" style="top:421px">
  <div class="date green"><b>31</b><i>mar</i></div>
  <h3>Varsity Boys’ Soccer match vs Ashford</h3>
  <p style="top:15px">Psum dolor sit amet, consectetuer adipiscing elit, sed diam nonummy nibh euismod..</p>
  <a style="top:37px">read more</a>
</article>
<article class="abs news" style="top:484px">
  <div class="date gold"><b>28</b><i>mar</i></div>
  <h3>Varsity Girls’ Tennis match vs Cedar Point</h3>
  <p style="top:29px">Psum dolor sit amet, consectetuer adipiscing elit, sed diam nonummy nibh euismod..</p>
  <a style="top:51px">read more</a>
</article>
<article class="abs news" style="top:557px">
  <div class="date gold"><b>12</b><i>mar</i></div>
  <h3>Lakemont Placement Test</h3>
  <p style="top:15px">The Lakemont Placement Test will be administered at KRA on Thursday, March 27, 2014. Please visit the School ...</p>
  <a style="top:37px">read more</a>
</article>
<article class="abs news" style="top:620px">
  <div class="date gold"><b>30</b><i>apr</i></div>
  <h3>Varsity Boys’ Home Soccer match vs Ashford</h3>
  <p style="top:29px">Psum dolor sit amet, consectetuer adipiscing elit, sed diam nonummy nibh euismod..</p>
  <a style="top:51px">read more</a>
</article>

<section class="abs events"></section>
<div class="abs notch"></div>
<h2 class="abs events-title blackletter">Upcoming Events</h2>

<article class="abs card" style="left:70px;top:795px">
  <div class="thumb" role="img" aria-label="Event poster photo of a classroom" style="background:linear-gradient(135deg,#6d8fb3,#d9cdb5)"></div>
  <h3>Meridian Responsive vCard - Pressly</h3>
  <span class="when">April 25, 2014</span>
  <p>Psum dolor sit amet, consectetuer adipiscing elit, sed diam nonummy nibh ang mga ibon euismod..</p>
</article>
<article class="abs card" style="left:348px;top:795px">
  <div class="thumb" role="img" aria-label="Event poster photo of a basketball game" style="background:linear-gradient(135deg,#d8c9a6,#7b6a3a)"></div>
  <h3>Brightline - One Page Pressly Creative Template</h3>
  <span class="when">April 07, 2014</span>
  <p>Psum dolor sit amet, consectetuer adipiscing elit, sed diam nonummy nibh ang mga ibon euismod..</p>
</article>
<article class="abs card" style="left:70px;top:891px">
  <div class="thumb" role="img" aria-label="Event poster photo of a stage performance" style="background:linear-gradient(135deg,#0c1a3a,#3d5a8a)"></div>
  <h3>Form - Responsive Pressly Theme</h3>
  <span class="when">April 25, 2014</span>
  <p>Psum dolor sit amet, consectetuer adipiscing elit, sed diam nonummy nibh ang mga ibon euismod..</p>
</article>
<article class="abs card" style="left:348px;top:891px">
  <div class="thumb" role="img" aria-label="Event poster photo of a piano recital" style="background:linear-gradient(135deg,#2a2420,#b8ad9c)"></div>
  <h3>Ripple Parallax One Page Pressly Theme</h3>
  <span class="when">March 28, 2014</span>
  <p>Psum dolor sit amet, consectetuer adipiscing elit, sed diam nonummy nibh ang mga ibon euismod..</p>
</article>

<footer class="abs footer"></footer>
<div class="abs fcol" style="left:75px">
  <h4>SITE NAV</h4>
  <ul><li>Home</li><li>Admissions</li><li>Staff Directory</li><li>Information Technology</li><li>Library</li><li>GradePortal (Teachers)</li></ul>
</div>
<div class="abs fcol" style="left:195px">
  <h4>HELP LINKS</h4>
  <ul><li>KRA Email</li><li>Online School Payments</li><li>Athletics</li><li>Documents/Forms</li><li>Contact Us</li><li>GradePortal (Parents/Students)</li></ul>
</div>
<div class="abs fcol" style="left:341px">
  <h4>PROGRAMS</h4>
  <div style="display:flex;gap:18px">
    <ul><li>Dance</li><li>Literary Arts</li><li>Music</li><li>Technology</li><li>Theatre Arts</li><li>Visual Arts</li></ul>
    <ul><li>English</li><li>Health and PE</li><li>Math</li><li>Science</li><li>Social Sciences</li><li>World Languages</li></ul>
  </div>
</div>
<div class="abs fcol" style="left:499px">
  <h4>CONNECT</h4>
  <div class="addr">9 Harbor Lane Studio<br>Eastfield, Lakemont 220418</div>
  <div class="phone">
    <svg width="15" height="15" viewBox="0 0 15 15"><circle cx="7.5" cy="7.5" r="6.5" fill="none" stroke="#cfd9cf" stroke-width="1"/><path d="M5 4.2l1.3-.4.9 2-.8.7c.4.9 1 1.5 1.9 1.9l.7-.8 2 .9-.4 1.3c-2.9.3-5.9-2.7-5.6-5.6z" fill="#cfd9cf"/></svg>
    0-98-7654321
  </div>
</div>

<div class="abs copyright">Copyright © 2013 Kelmont Regional Academy</div>
<div class="abs social" aria-label="Social links"><span></span><span></span><span></span><span></span><span></span></div>

</body>
</html>
```